Marlow Crest Group (Real Estate and Investment)

A high end, clean design.
We are a real estate company with sales, asset management and investment divisions. We want to use a black and white scheme which is really high end feel. The back of the card can just be the logo (black background with the white writing) as we will probably emboss this when we print)

Target Market(s)

High level investors, high end houses for sale

Industry/Entity Type

Business

Contact Information for Business Card

Name, position, phone number and email address
Glen Varley, Managing Director, 0437259064 and glen@marlowcrest-example.com.au

Requirements
Must have
• Back of the card to be the black background with the white writing (as per the attached images). Would like the capacity to emboss the writing and logo

```html
<!DOCTYPE html>
<html lang="en">
<head>
<meta charset="utf-8">
<title>Marlow Crest Group – Business Card</title>
<link rel="stylesheet" href="https://fonts.googleapis.com/css2?family=Open+Sans:ital,wght@0,400;0,600;1,400&display=swap">
<style>
  :root {
    --backdrop: #d9d9d9;
    --paper: #ffffff;
    --ink: #231f20;
    --ink-soft: #3a3a3a;
    --stone: #7f7f7f;
    --rule: #333333;
  }
  * { margin: 0; padding: 0; box-sizing: border-box; }
  html, body {
    width: 1200px; height: 987px; overflow: hidden;
    background: var(--backdrop);
    font-family: "Open Sans", Arial, sans-serif;
    color: var(--ink);
  }
  .canvas { position: relative; width: 1200px; height: 987px; }

  .card {
    position: absolute; left: 293px; width: 616px; height: 352px; overflow: hidden;
  }
  .card-front { top: 130px; background: var(--paper); }
  .card-back  { top: 505px; background: var(--stone); }

  .brand-mark {
    position: absolute; left: 732px; top: 29px; /* relative to card */
  }
  .card-front .brand-mark { left: 439px; top: 29px; width: 88px; height: 88px; }
  .brand-name {
    position: absolute; right: 30px; top: 138px;
    font-size: 21px; font-weight: 400; letter-spacing: -0.2px;
    text-transform: uppercase; color: var(--ink); white-space: nowrap;
  }
  .person-name {
    position: absolute; left: 27px; top: 222px;
    font-size: 22px; font-weight: 600; color: var(--ink);
  }
  .name-rule {
    position: absolute; left: 27px; right: 30px; top: 258px;
    border-top: 1.5px solid var(--rule);
  }
  .contact-list {
    position: absolute; left: 27px; top: 272px; list-style: none;
    font-size: 14px; line-height: 24px; color: var(--ink-soft);
  }
  .contact-list li { display: flex; align-items: center; gap: 7px; }
  .contact-list svg { width: 13px; height: 13px; fill: var(--ink); flex: none; }
  .website {
    position: absolute; right: 30px; top: 296px;
    font-size: 14px; font-style: italic; line-height: 24px; color: var(--ink-soft);
  }
  .edge-band { position: absolute; left: 0; bottom: 0; width: 616px; height: 13px; }

  .back-art { position: absolute; inset: 0; }
</style>
</head>
<body>
<main class="canvas">

  <section class="card card-front" aria-label="Card front">
    <svg class="brand-mark" viewBox="0 0 88 88" aria-hidden="true">
      <circle cx="44" cy="44" r="42" fill="none" stroke="var(--ink)" stroke-width="1.6"/>
    </svg>
    <p class="brand-name">Marlow Crest Group</p>

    <h1 class="person-name">Glen Varley</h1>
    <div class="name-rule"></div>

    <ul class="contact-list">
      <li>
        <svg viewBox="0 0 24 24" aria-hidden="true"><path d="M6.6 10.8a15.1 15.1 0 0 0 6.6 6.6l2.2-2.2c.3-.3.7-.4 1-.2 1.1.4 2.3.6 3.6.6.6 0 1 .4 1 1V20c0 .6-.4 1-1 1A17 17 0 0 1 3 4c0-.6.4-1 1-1h3.5c.6 0 1 .4 1 1 0 1.3.2 2.5.6 3.6.1.3 0 .7-.2 1z"/></svg>
        <span>0437259064</span>
      </li>
      <li>
        <svg viewBox="0 0 24 24" aria-hidden="true"><path d="M2 5h20v14H2z M2 5l10 8 10-8" fill="var(--ink)"/><path d="M3 6l9 7 9-7" fill="none" stroke="var(--paper)" stroke-width="1.6"/></svg>
        <span>glen@marlowcrest-example.com.au</span>
      </li>
    </ul>
    <p class="website">www.marlowcrest-example.com.au</p>

    <svg class="edge-band" viewBox="0 0 616 13" preserveAspectRatio="none" aria-hidden="true">
      <rect x="0" y="0" width="616" height="13" fill="var(--stone)"/>
      <polygon points="0,0 404,0 399,13 0,13" fill="var(--ink)"/>
      <polygon points="404,0 407,0 402,13 399,13" fill="var(--paper)"/>
    </svg>
  </section>

  <section class="card card-back" aria-label="Card back">
    <svg class="back-art" viewBox="0 0 616 352" aria-hidden="false">
      <circle cx="424" cy="175" r="186" fill="var(--ink)" stroke="var(--paper)" stroke-width="7"/>
      <text class="back-brand" transform="translate(88 326) rotate(-90)"
            font-family="'Open Sans', Arial, sans-serif" font-size="26" font-weight="400"
            fill="var(--paper)" letter-spacing="-0.3">MARLOW CREST GROUP</text>
      <text class="back-website" transform="translate(117 326) rotate(-90)"
            font-family="'Open Sans', Arial, sans-serif" font-size="13" font-style="italic"
            fill="var(--paper)" letter-spacing="1.6">www.marlowcrest-example.com.au</text>
    </svg>
  </section>

</main>
</body>
</html>
```